Design a Unique and Eye-Catching Necklace Card for Verandelle's New Lumenwave Line

Attention all creative minds from around the world! Verandelle, a company known for its free-spirited and bohemian chic vibe, is proud to announce a new design contest. We are inviting you to create a dynamic and unique necklace card for our upcoming Lumenwave line.

Our new Lumenwave line comprises 12-20 unique necklace combinations. Each necklace features different stones, each with its own healing properties and associated zodiac sign. We are looking for a template that can be easily modified to change the names of the stones, zodiac sign, and the colors to match the specific stones on each necklace.

The card should be 3 x 4,
It should include the names of the stones, the associated zodiac sign (if applicable), a few words about the healing properties of the stones, and a captivating graphic that represents the colors of the stones.

Our goal is to delight our customers with packaging as unique as the necklaces themselves. The necklace should be the focal point, but the text and graphic on the card should also draw the eye.

Please note that our target audience includes mid-priced boutiques across the country and festival-goers in Colorado. Your design should reflect the unique taste and free spirit of our clientele.

We are excited to see your creativity shine in this project. If there are any points that need clarification, please do not hesitate to ask. We look forward to your participation in bringing the Lumenwave line to life!
https://www.plorvex.example/board/QKTm_ZRwpe/u3hb9XKdLqWm72RtPoaVnc/edit?ref=QKTm_ZRwpe&src=share

https://www.plorvex.example/board/QKTr_BNyhwa/t8Ld-WsPzMEY246VqoXjNd/edit?ref=QKTr_BNyhwa&src=share
I want to use the flowing watercolor and have it change with each necklace color.
Use the necklaces below. Incorporate the zodiac symbol as is shown below.

Examples of other cards in our collection

The Little Pebble Pendant: https://www.plorvex.example/board/QKTh_WomRtc/pbMRx63CKqnYs905Bd-aLe/edit?ref=QKTh_WomRtc&src=share

Other examples of necklace cards I like:

https://www.tindramart.example/item/731920584/green-emerald-stone-necklace-emerald?k=a1b2c3d4e5f60718293a4b5c6d7e8f9012345678&s=7d3e91ab

https://www.tindramart.example/item/846201937/january-birthstone-necklace-green-garnet?k=b2c3d4e5f60718293a4b5c6d7e8f901234567890&s=4c82fe10

https://www.tindramart.example/item/2093748165/natural-crystal-bracelets-empath?k=c3d4e5f60718293a4b5c6d7e8f90123456789012&s=9ab0c37d

https://www.tindramart.example/item/2174603958/black-obsidian-protection-necklace-black?k=d4e5f60718293a4b5c6d7e8f9012345678901234&s=e15d6b28

Target Market(s)

Women aged 25-50 with a spiritual, hippy, bohemain, yoga vibe.

Industry/Entity Type

Handmade Jewelry | Wholesale jewelry | Retail Jewelry sales at Festivals

Font styles to use
Script

Colors

Designer to choose colors to be used in the design.

Requirements
Must have
• A template that can be interchangable with the stone colors, names and healing properties.
Nice to have
• Some different ideas about the graphic color patterns on the card.
Should not have
• Any graphic that would cover the middle of the necklace card and keep people from seeing the neckalce

```html
<!DOCTYPE html>
<html lang="en">
<head>
<meta charset="utf-8">
<title>Verandelle Lumenwave Necklace Cards</title>
<link rel="stylesheet" href="https://fonts.googleapis.com/css2?family=Parisienne&family=Noto+Sans+Symbols&display=swap">
<style>
  :root {
    --stage: #3b3b3b;
    --card-w: 237px;
    --card-h: 309px;
    --script: "Parisienne", cursive;
    --glyph: "Noto Sans Symbols", sans-serif;
  }
  * { box-sizing: border-box; margin: 0; padding: 0; }
  html, body { width: 1200px; height: 1200px; overflow: hidden; background: var(--stage); }
  .stage { position: relative; width: 1200px; height: 1200px; }

  .card {
    position: absolute;
    width: var(--card-w);
    height: var(--card-h);
    background: var(--bg);
    color: var(--ink);
    box-shadow: 0 6px 18px rgba(0,0,0,.45);
    overflow: hidden;
    font-family: var(--script);
    text-align: center;
  }
  .stones {
    position: absolute; top: 22px; left: 0; right: 0;
    font-size: 19px; line-height: 1.2; white-space: nowrap;
  }
  .stones .plus { font-size: 11px; margin: 0 4px; vertical-align: 3px; }
  .sign-badge {
    position: absolute; top: 60px; left: 50%;
    width: 26px; height: 26px; margin-left: -13px;
    border-radius: 50%; background: var(--badge, var(--ink));
    color: #fff; font-family: var(--glyph); font-size: 15px; line-height: 26px;
  }
  .sign-name {
    position: absolute; top: 90px; left: 0; right: 0;
    font-size: 19px;
  }
  .property {
    position: absolute; top: 207px; left: 40px; right: 40px;
    font-size: 13px; line-height: 1.4; z-index: 2;
  }
  .wash {
    position: absolute; left: 0; bottom: 0;
    width: var(--card-w); height: 94px; display: block;
  }

  .pisces-aqua    { left: 160px; top: 68px;  --bg:#d4edfb; --ink:#2b3a8a; }
  .capricorn      { left: 474px; top: 68px;  --bg:#fff2e2; --ink:#4a2e1a; }
  .virgo          { left: 788px; top: 68px;  --bg:#e4f3fc; --ink:#5d6457; }
  .sag-turquoise  { left: 160px; top: 447px; --bg:#f5f9df; --ink:#6b2f27; }
  .sag-hessonite  { left: 476px; top: 447px; --bg:#eaf7f4; --ink:#2c2622; --badge:#4b2e17; }
  .gemini         { left: 788px; top: 447px; --bg:#dbdfd1; --ink:#5e6656; }
  .sag-pietersite { left: 312px; top: 823px; --bg:#c5dcdb; --ink:#4e4944; --badge:#5a524b; }
  .pisces-fluorite{ left: 626px; top: 823px; --bg:#f5ebd2; --ink:#33205f; }
</style>
</head>
<body>
<main class="stage">

  <svg width="0" height="0" style="position:absolute" aria-hidden="true">
    <defs>
      <linearGradient id="wash-blue" x1="0" x2="1"><stop offset=".35" stop-color="#7f97a3"/><stop offset=".6" stop-color="#74aee0"/></linearGradient>
      <linearGradient id="wash-ember" x1="0" x2="1"><stop offset=".35" stop-color="#3b6e68"/><stop offset=".6" stop-color="#e88a30"/></linearGradient>
      <linearGradient id="wash-sun" x1="0" x2="1"><stop offset=".35" stop-color="#f7b84a"/><stop offset=".6" stop-color="#6dbfa6"/></linearGradient>
      <linearGradient id="wash-teal" x1="0" x2="1"><stop offset=".35" stop-color="#2a9594"/><stop offset=".6" stop-color="#a8824a"/></linearGradient>
      <linearGradient id="wash-red" x1="0" x2="1"><stop offset=".35" stop-color="#e83a24"/><stop offset=".6" stop-color="#86c47f"/></linearGradient>
      <linearGradient id="wash-sky" x1="0" x2="1"><stop offset=".35" stop-color="#57c3d4"/><stop offset=".6" stop-color="#7b7a48"/></linearGradient>
      <linearGradient id="wash-peach" x1="0" x2="1"><stop offset=".35" stop-color="#f8ab6a"/><stop offset=".6" stop-color="#c17a55"/></linearGradient>
      <linearGradient id="wash-violet" x1="0" x2="1"><stop offset=".35" stop-color="#ab64a6"/><stop offset=".6" stop-color="#a0aca6"/></linearGradient>
      <path id="wave" d="M0,10 C20,-2 30,30 50,35 C75,40 70,70 100,68 C130,66 150,62 170,45 C190,30 215,40 237,33 L237,94 L0,94 Z"/>
    </defs>
  </svg>

  <article class="card pisces-aqua">
    <h2 class="stones">Aquamarine<span class="plus">+</span>Kyanite</h2>
    <div class="sign-badge">&#9811;&#xFE0E;</div>
    <p class="sign-name">Pisces</p>
    <p class="property">Reduce Stress &amp; Anxiety</p>
    <svg class="wash" viewBox="0 0 237 94" role="img" aria-label="Flowing watercolor wash with leaf line art in grey blue and sky blue"><use href="#wave" fill="url(#wash-blue)"/></svg>
  </article>

  <article class="card capricorn">
    <h2 class="stones">Ocean Jasper</h2>
    <div class="sign-badge">&#9809;&#xFE0E;</div>
    <p class="sign-name">Capricorn</p>
    <p class="property">Alleviates Depression &amp; Stress</p>
    <svg class="wash" viewBox="0 0 237 94" role="img" aria-label="Flowing watercolor wash with leaf line art in deep teal and orange"><use href="#wave" fill="url(#wash-ember)"/></svg>
  </article>

  <article class="card virgo">
    <h2 class="stones">Turquoise<span class="plus">+</span>Amazonite</h2>
    <div class="sign-badge">&#9805;&#xFE0E;</div>
    <p class="sign-name">Virgo</p>
    <p class="property">Shields from Electromagnetic Pollution</p>
    <svg class="wash" viewBox="0 0 237 94" role="img" aria-label="Flowing watercolor wash with leaf line art in golden yellow and sea green"><use href="#wave" fill="url(#wash-sun)"/></svg>
  </article>

  <article class="card sag-turquoise">
    <h2 class="stones">Turquoise</h2>
    <div class="sign-badge">&#9808;&#xFE0E;</div>
    <p class="sign-name">Sagittarius</p>
    <p class="property">Helpful for clarity &amp; self - expression</p>
    <svg class="wash" viewBox="0 0 237 94" role="img" aria-label="Flowing watercolor wash with leaf line art in teal and ochre"><use href="#wave" fill="url(#wash-teal)"/></svg>
  </article>

  <article class="card sag-hessonite">
    <h2 class="stones">Turquoise<span class="plus">+</span>Hessonite</h2>
    <div class="sign-badge">&#9808;&#xFE0E;</div>
    <p class="sign-name">Sagittarius</p>
    <p class="property">Anti Inflammatory &amp; Reduces Pain from Arthritis</p>
    <svg class="wash" viewBox="0 0 237 94" role="img" aria-label="Flowing watercolor wash with leaf line art in red and soft green"><use href="#wave" fill="url(#wash-red)"/></svg>
  </article>

  <article class="card gemini">
    <h2 class="stones">Chrysocolla<span class="plus">+</span>Aquamarine</h2>
    <div class="sign-badge">&#9802;&#xFE0E;</div>
    <p class="sign-name">Gemini</p>
    <p class="property">Detoxifies the Liver, Kidneys, and Intestines</p>
    <svg class="wash" viewBox="0 0 237 94" role="img" aria-label="Flowing watercolor wash with leaf line art in sky blue and olive"><use href="#wave" fill="url(#wash-sky)"/></svg>
  </article>

  <article class="card sag-pietersite">
    <h2 class="stones">Pietersite</h2>
    <div class="sign-badge">&#9808;&#xFE0E;</div>
    <p class="sign-name">Sagittarius</p>
    <p class="property">Increase Will Power &amp; Fortitude</p>
    <svg class="wash" viewBox="0 0 237 94" role="img" aria-label="Flowing watercolor wash with leaf line art in peach and terracotta"><use href="#wave" fill="url(#wash-peach)"/></svg>
  </article>

  <article class="card pisces-fluorite">
    <h2 class="stones">Fluorite</h2>
    <div class="sign-badge">&#9811;&#xFE0E;</div>
    <p class="sign-name">Pisces</p>
    <p class="property">Improves Decision Making</p>
    <svg class="wash" viewBox="0 0 237 94" role="img" aria-label="Flowing watercolor wash with leaf line art in violet and sage grey"><use href="#wave" fill="url(#wash-violet)"/></svg>
  </article>

</main>
</body>
</html>
```